Design a Website Mockup for Horse Stable

See Attachement for Logo.
Style should be very luxery / established / powerful and fit the style of the logo.
Please include the Yellow/Blue colors of the logo.

You can use the pictures attached for the drafts.

Thank you

```html
<!DOCTYPE html>
<html lang="en">
<head>
<meta charset="utf-8">
<title>Gut Lindenhof – Horse Stable</title>
<link rel="stylesheet" href="https://fonts.googleapis.com/css2?family=Open+Sans:wght@300;400;600;700&display=swap">
<style>
  :root{
    --navy:#0d3f7c;
    --blue:#1858a3;
    --blue-deep:#0c3a73;
    --gold:#e6cf6a;
    --gold-line:#d9c35a;
    --olive:#a5b84a;
    --green:#8aa42a;
    --sky:#abdce6;
    --card:#f2f2f2;
    --ink:#222;
    --footer:#2b2b2b;
    --field:#454545;
    --muted:#bdbdbd;
  }
  *{box-sizing:border-box;margin:0;padding:0}
  html,body{width:1169px;height:1200px;overflow:hidden}
  body{position:relative;font-family:"Open Sans",Arial,sans-serif;background:#fff;color:var(--ink)}
  .abs{position:absolute}

  /* header */
  .topbar{left:0;top:0;width:1169px;height:61px;background:linear-gradient(#1a5aa2,#0f4585);border-bottom:2px solid var(--gold-line)}
  .language{left:886px;top:20px;font-size:9px;color:#fff;display:flex;align-items:center;gap:6px}
  .flag{width:17px;height:11px;display:block}
  .navbar{left:0;top:63px;width:1169px;height:57px;background:linear-gradient(#154c8d,#0b3468)}
  .nav-link{top:77px;font-size:18px;font-weight:300;color:var(--gold);text-transform:uppercase;letter-spacing:.2px}

  .brand-panel{left:490px;top:0;width:197px;height:214px;background:linear-gradient(#ffffff,#e4e4e4);border-bottom:4px solid var(--gold-line);box-shadow:0 2px 6px rgba(0,0,0,.35);display:flex;align-items:center;justify-content:center;z-index:3}
  .brand-name{font-size:21px;font-weight:600;color:var(--navy);text-align:center;line-height:1.2}

  /* slider */
  .slider{left:0;top:120px;width:1169px;height:345px;background:#555}
  .slide-side{top:120px;height:345px;background:linear-gradient(#4a4a4a,#2e2e2e)}
  .slide-main{left:99px;top:120px;width:996px;height:345px;background:linear-gradient(#9c7d62 0%,#6f6a4a 30%,#4d7a3a 55%,#6aa23f 80%,#7fb24a 100%)}
  .arrow{top:270px;width:22px;height:44px}

  /* intro band */
  .intro{left:0;top:465px;width:1169px;height:166px;background:linear-gradient(#155297,#0e4687)}
  .intro-head{left:0;top:465px;width:1169px;height:58px;background:#1a5ea8;display:flex;align-items:center;justify-content:center}
  .intro-head h1{font-size:23px;font-weight:700;color:#fff}
  .intro-text{left:0;top:536px;width:1169px;text-align:center;font-size:14px;line-height:19.5px;color:#b8cde6;font-weight:400}

  /* news */
  .section-title{left:191px;top:652px;font-size:23px;font-weight:300;color:var(--olive);text-transform:uppercase}
  .card{top:701px;width:236px}
  .card-photo{height:120px}
  .card-body{height:82px;background:var(--card);padding:6px 8px 0 9px;font-size:10.2px;line-height:13.6px;letter-spacing:-.1px;color:#222}
  .card-more{height:34px;background:var(--sky);display:flex;align-items:center;padding-left:10px;font-size:12px;font-weight:700;color:#1d2a30;gap:8px}

  /* footer */
  .footer{left:0;top:972px;width:1169px;height:228px;background:var(--footer);box-shadow:inset 0 8px 8px -6px #000}
  .footer-label{font-size:10px;font-weight:700;color:#fff}
  .newsletter-input{left:181px;top:1018px;width:176px;height:28px;background:var(--field)}
  .btn{background:var(--green);color:#1b1b1b;font-size:10.5px;text-transform:uppercase;display:flex;align-items:center;justify-content:center}
  .social{top:1107px;width:23px;height:23px;border-radius:50%}
  .links{font-size:9px;line-height:16px;color:#c9c9c9;list-style:none}
  .links li::before{content:"";display:inline-block;width:4px;height:4px;border-radius:50%;background:var(--green);margin-right:6px;vertical-align:middle}
  .contact-title{left:764px;top:992px;font-size:14px;font-weight:600;color:#fff}
  .field{left:762px;width:241px;background:var(--field);font-size:9.5px;font-weight:700;color:#fff;padding:4px 8px}
</style>
</head>
<body>

<header>
  <div class="abs topbar"></div>
  <div class="abs language">
    <span>Select Language</span>
    <svg class="flag" viewBox="0 0 17 11" aria-label="English">
      <rect width="17" height="11" fill="#1f3f8f"/>
      <path d="M0 0L17 11M17 0L0 11" stroke="#fff" stroke-width="2"/>
      <path d="M0 0L17 11M17 0L0 11" stroke="#c8102e" stroke-width=".8"/>
      <path d="M8.5 0V11M0 5.5H17" stroke="#fff" stroke-width="3"/>
      <path d="M8.5 0V11M0 5.5H17" stroke="#c8102e" stroke-width="1.6"/>
    </svg>
    <svg class="flag" viewBox="0 0 17 11" aria-label="Deutsch">
      <rect width="17" height="3.7" fill="#000"/>
      <rect y="3.7" width="17" height="3.7" fill="#dd0000"/>
      <rect y="7.4" width="17" height="3.6" fill="#ffce00"/>
    </svg>
  </div>
  <div class="abs navbar"></div>
  <nav>
    <span class="abs nav-link" style="left:134px">Home</span>
    <span class="abs nav-link" style="left:239px">About us</span>
    <span class="abs nav-link" style="left:375px">Gallery</span>
    <span class="abs nav-link" style="left:708px">Events</span>
    <span class="abs nav-link" style="left:823px">Horses</span>
    <span class="abs nav-link" style="left:942px">Contact</span>
  </nav>
  <div class="abs brand-panel"><span class="brand-name">Gut Lindenhof</span></div>
</header>

<section>
  <div class="abs slider"></div>
  <div class="abs slide-side" style="left:0;width:98px" role="img" aria-label="Previous slide: dark horse portrait"></div>
  <div class="abs slide-side" style="left:1096px;width:73px" role="img" aria-label="Next slide: stable building"></div>
  <div class="abs slide-main" role="img" aria-label="Group of horses grazing on a green paddock in front of a hedge and stable"></div>
  <svg class="abs arrow" style="left:12px" viewBox="0 0 22 44"><path d="M18 4L4 22L18 40" fill="none" stroke="#d8d8d8" stroke-width="5"/></svg>
  <svg class="abs arrow" style="left:1134px" viewBox="0 0 22 44"><path d="M4 4L18 22L4 40" fill="none" stroke="#d8d8d8" stroke-width="5"/></svg>
</section>

<section>
  <div class="abs intro"></div>
  <div class="abs intro-head"><h1>The standard Lorem Ipsum passage, used since the 1500s</h1></div>
  <p class="abs intro-text">Lorem ipsum dolor sit amet, consectetur adipiscing elit. Nullam tincidunt scelerisque urna, et varius eros aliquam vel.<br>Cras convallis facilisis dolor, nec sodales sem posuere eget. Phasellus pulvinar adipiscing felis, et pharetra odio consectetur facilisis.<br>Aliquam non tempus enim. Vestibulum sagittis mauris vel justo auctor, quis sodales nisl iaculis.</p>
</section>

<section>
  <h2 class="abs section-title">News and Events</h2>

  <article class="abs card" style="left:191px">
    <div class="card-photo" role="img" aria-label="Horses grazing in front of a brick stable" style="background:linear-gradient(#a5816a 0%,#8b7a5a 45%,#5f8a3c 70%,#78b040 100%)"></div>
    <p class="card-body">Lorem ipsum dolor sit amet, consectetur adipiscing elit. Nunc fringilla sit amet urna ut fermentum. Curabitur mollis consequat ullamcorper. Vestibulum eget condimentum urna. Nam dapibus lacus fringilla</p>
    <div class="card-more"><svg width="7" height="10" viewBox="0 0 7 10"><path d="M1 1L5.5 5L1 9" fill="none" stroke="#1d2a30" stroke-width="2"/></svg>Read More</div>
  </article>

  <article class="abs card" style="left:461px">
    <div class="card-photo" role="img" aria-label="Carved estate sign between trees" style="background:linear-gradient(#8fb2d6 0%,#b9a88a 40%,#8a7b62 70%,#5e7f3e 100%)"></div>
    <p class="card-body">Lorem ipsum dolor sit amet, consectetur adipiscing elit. Nunc fringilla sit amet urna ut fermentum. Curabitur mollis consequat ullamcorper. Vestibulum eget condimentum urna. Nam dapibus lacus fringilla</p>
    <div class="card-more"><svg width="7" height="10" viewBox="0 0 7 10"><path d="M1 1L5.5 5L1 9" fill="none" stroke="#1d2a30" stroke-width="2"/></svg>Read More</div>
  </article>

  <article class="abs card" style="left:733px">
    <div class="card-photo" role="img" aria-label="Brick country house under a blue sky" style="background:linear-gradient(#4f87cc 0%,#7fa6d6 35%,#9a6a52 60%,#6b7a56 100%)"></div>
    <p class="card-body">Lorem ipsum dolor sit amet, consectetur adipiscing elit. Nunc fringilla sit amet urna ut fermentum. Curabitur mollis consequat ullamcorper. Vestibulum eget condimentum urna. Nam dapibus lacus fringilla</p>
    <div class="card-more"><svg width="7" height="10" viewBox="0 0 7 10"><path d="M1 1L5.5 5L1 9" fill="none" stroke="#1d2a30" stroke-width="2"/></svg>Read More</div>
  </article>
</section>

<footer>
  <div class="abs footer"></div>
  <span class="abs footer-label" style="left:181px;top:1002px">Newsletter signup</span>
  <div class="abs newsletter-input"></div>
  <div class="abs btn" style="left:292px;top:1046px;width:65px;height:22px">Submit</div>

  <span class="abs social" style="left:184px;background:#3fb6d8"></span>
  <span class="abs social" style="left:221px;background:#4a64a6"></span>
  <span class="abs social" style="left:258px;background:#4a4a4a"></span>
  <span class="abs social" style="left:296px;background:#2f7fb4"></span>
  <span class="abs social" style="left:333px;background:#f08a24"></span>

  <ul class="abs links" style="left:417px;top:1007px">
    <li>Home</li><li>About us</li><li>Gallery</li><li>News and Events</li><li>Horses</li><li>Contact</li>
  </ul>
  <ul class="abs links" style="left:533px;top:1007px">
    <li>Site map</li><li>Terms &amp; Conditions</li><li>Privacy policy</li><li>Resources</li>
  </ul>

  <span class="abs contact-title">Quick Contact</span>
  <div class="abs field" style="top:1020px;height:23px">Name</div>
  <div class="abs field" style="top:1044px;height:22px">Email</div>
  <div class="abs field" style="top:1068px;height:57px">Message</div>
  <div class="abs btn" style="left:925px;top:1128px;width:78px;height:22px">Submit</div>
</footer>

</body>
</html>
```